Business card for Harbor Crafters
Looking for creativity
Professional
Dominic Farrow
Owner Operator
47 S Pell Avenue
Brookhaven, MD 19842
@domfarrow
craftharborco@mailvane.com
www.craftharborco.com
Looking for a creative business card for my company. I have a logo and like the feel of it. The business card should have a contemporary feel and be interesting.
The name of the company and the website

```html
<!DOCTYPE html>
<html lang="en">
<head>
<meta charset="utf-8">
<title>Harbor Crafters — Business Card</title>
<link rel="stylesheet" href="https://fonts.googleapis.com/css2?family=Montserrat:wght@400;500;600&family=Open+Sans:wght@400;600&display=swap">
<style>
  :root {
    --backdrop: #e9e4dc;
    --card-white: #ffffff;
    --brand-blue: #1c57a9;
    --swoosh-grey: #b9bcc2;
    --swoosh-light: #dfe1e5;
    --text-white: #ffffff;
    --logo-silver: #d6dbe3;
  }
  * { box-sizing: border-box; margin: 0; padding: 0; }
  html, body {
    width: 1200px; height: 559px; overflow: hidden;
    background: var(--backdrop);
  }
  .canvas { position: relative; width: 1200px; height: 559px; }
  .card {
    position: absolute; top: 100px;
    width: 492px; height: 370px;
    overflow: hidden;
    box-shadow: 0 4px 14px rgba(0,0,0,0.18);
  }
  .card--front { left: 96px; background: var(--card-white); }
  .card--back { left: 628px; background: var(--brand-blue); }
  .card__shape { position: absolute; inset: 0; width: 100%; height: 100%; }

  .brand-name {
    position: absolute;
    font-family: "Montserrat", sans-serif;
    font-weight: 600;
    text-transform: uppercase;
    text-align: center;
    letter-spacing: 3px;
    line-height: 1.15;
    white-space: nowrap;
  }
  .card--front .brand-name {
    left: 14px; width: 196px; top: 140px;
    font-size: 22px; color: var(--brand-blue);
  }
  .card--back .brand-name {
    left: 0; width: 100%; top: 138px;
    font-size: 30px; color: var(--logo-silver);
  }
  .brand-name__mark {
    display: block; width: 14px; height: 14px; margin: 0 auto 8px;
    border-radius: 50%; background: currentColor;
  }
  .card--back .brand-name__mark { width: 16px; height: 16px; margin-bottom: 10px; }

  .contact {
    position: absolute; right: 32px; text-align: right;
    font-family: "Open Sans", sans-serif; color: var(--text-white);
  }
  .contact__name { top: 68px; font-family: "Montserrat", sans-serif; font-size: 19px; font-weight: 500; }
  .contact__role { top: 96px; font-size: 12px; }
  .contact__address { top: 138px; font-size: 12.5px; line-height: 20px; }
  .contact__list { top: 220px; list-style: none; font-size: 12.5px; }
  .contact__list li { display: flex; justify-content: flex-end; align-items: center; height: 24px; gap: 8px; }
  .contact__icon { width: 13px; height: 13px; flex: none; }

  .website {
    position: absolute; left: 0; width: 100%; top: 280px; text-align: center;
    font-family: "Open Sans", sans-serif; font-size: 12px; letter-spacing: 4px;
    color: var(--text-white);
  }
</style>
</head>
<body>
<main class="canvas">

  <section class="card card--front" aria-label="Card front">
    <svg class="card__shape" viewBox="0 0 492 370" preserveAspectRatio="none" aria-hidden="true">
      <path d="M258 0 C224 110 224 250 262 370 L492 370 L492 0 Z" fill="var(--brand-blue)"/>
      <path d="M250 0 C214 110 214 250 254 370 L262 370 C224 250 224 110 258 0 Z" fill="var(--swoosh-grey)"/>
    </svg>
    <div class="brand-name"><span class="brand-name__mark"></span>Harbor<br>Crafters</div>

    <div class="contact contact__name">Dominic Farrow</div>
    <div class="contact contact__role">Owner Operator</div>
    <div class="contact contact__address">47 S Pell Avenue<br>Brookhaven, MD 19842</div>
    <ul class="contact contact__list">
      <li>302.555.0148
        <svg class="contact__icon" viewBox="0 0 16 16" aria-hidden="true"><path d="M3 1.5l3 .5 1 3.5-2 1.2a8 8 0 0 0 4.3 4.3l1.2-2 3.5 1 .5 3c-7 1-12.5-4.5-11.5-11.5z" fill="#fff"/></svg>
      </li>
      <li>@domfarrow
        <svg class="contact__icon" viewBox="0 0 16 16" aria-hidden="true"><circle cx="8" cy="8" r="6.5" fill="#fff"/></svg>
      </li>
      <li>craftharborco@mailvane.com
        <svg class="contact__icon" viewBox="0 0 16 16" aria-hidden="true"><circle cx="8" cy="8" r="3" fill="none" stroke="#fff" stroke-width="1.8"/><path d="M11 5v4.5a2 2 0 0 0 4 0V8a7 7 0 1 0-3 5.7" fill="none" stroke="#fff" stroke-width="1.8"/></svg>
      </li>
      <li>www.craftharborco.com
        <svg class="contact__icon" viewBox="0 0 16 16" aria-hidden="true"><circle cx="8" cy="8" r="6.5" fill="none" stroke="#fff" stroke-width="1.5"/><ellipse cx="8" cy="8" rx="3" ry="6.5" fill="none" stroke="#fff" stroke-width="1.2"/><path d="M1.5 8h13" stroke="#fff" stroke-width="1.2"/></svg>
      </li>
    </ul>
  </section>

  <section class="card card--back" aria-label="Card back">
    <svg class="card__shape" viewBox="0 0 492 370" preserveAspectRatio="none" aria-hidden="true">
      <path d="M0 0 L14 0 C-4 120 -4 250 16 370 L0 370 Z" fill="var(--swoosh-grey)"/>
      <path d="M14 0 L20 0 C2 120 2 250 22 370 L16 370 C-4 250 -4 120 14 0 Z" fill="var(--swoosh-light)"/>
    </svg>
    <div class="brand-name"><span class="brand-name__mark"></span>Harbor Crafters</div>
    <div class="website">www.craftharborco.com</div>
  </section>

</main>
</body>
</html>
```